WP website design Pine Harbor (Contest)

We need a wordpress design that will incorporate a professional color scheme with company logo in a clean layout. The design needs to consider that this will be developed on a responsive theme. Colors are blue and green of the logo and and an accent color (perhaps very light brown/tan). Client wants a 'modern' look.

Industry/Entity Type

It Company

Font styles to use
Serif
Sans Serif

Colors

Designer to choose colors to be used in the design.

Requirements
Must have
• Navigation: 1) Home; 2) Upcoming Auctions; 3) Past Auctions; 4) About Us; 5) Services; 6) Sellers; 7) Buyers; 8) Contact Us

Site will have slideshow - image is attached. Colors will be those in the logo, blue and green with maybe an accent color. A site the client mentions liking is trevalleauctions.com for the use of color and layout.

Widgets: 1) Featured Properties; 2) Call to action for Sellers 3) Testimonials blog/widget
Nice to have
• use of dropdown menus

```html
<!DOCTYPE html>
<html lang="en">
<head>
<meta charset="utf-8">
<title>Pine Harbor Auction &amp; Real Estate</title>
<link rel="stylesheet" href="https://fonts.googleapis.com/css2?family=Arimo:wght@400;700&family=Source+Sans+3:wght@400;600;700&family=Fjalla+One&display=swap">
<style>
:root{
  --navy:#0b3f7d;
  --navy-dark:#062d5e;
  --navy-light:#1d5596;
  --green:#006633;
  --green-dark:#004d26;
  --red-top:#7a271f;
  --red-bottom:#451510;
  --panel:#efefef;
  --panel-line:#b9b9b9;
  --ink:#222;
  --alert:#e2173a;
  --footer-mark:#d9d0cd;
}
*{box-sizing:border-box;margin:0;padding:0}
html,body{width:1022px;height:1200px;overflow:hidden}
body{background:linear-gradient(var(--red-top),var(--red-bottom));font-family:Arimo,Arial,sans-serif;color:var(--ink)}
.stage{position:relative;width:1200px;height:1409px;transform:scale(.85167);transform-origin:0 0}
.abs{position:absolute}
.page{left:100px;top:0;width:1000px;height:1268px;background:#fff}

.header{left:100px;top:0;width:1000px;height:318px;background:#efefef}
.hero{left:300px;top:0;width:800px;height:318px;
  background:linear-gradient(180deg,#9b7a78 0%,#a78c86 35%,#8da0a0 50%,#a9b8c2 58%,#5f8f3c 66%,#3d7a2a 100%);}
.hero-fade{left:300px;top:0;width:180px;height:318px;background:linear-gradient(90deg,#efefef 10%,rgba(239,239,239,0))}
.brand{left:130px;top:38px;display:flex;align-items:center;gap:12px}
.brand-dot{width:58px;height:58px;border-radius:50%;background:var(--navy)}
.brand-name{font-family:"Source Sans 3",sans-serif;font-weight:700;font-size:31px;line-height:33px;color:var(--navy)}
.brand-rule{left:130px;top:164px;width:230px;height:3px;background:var(--green)}
.site-name{left:130px;top:180px;width:256px;text-align:center;font-family:"Fjalla One",sans-serif;font-size:30px;line-height:35px;color:var(--green)}

.nav{left:100px;top:318px;width:1000px;height:52px;background:linear-gradient(var(--navy),var(--navy-dark));display:flex}
.nav a{display:block;height:52px;line-height:52px;padding:0 20px;color:#fff;text-decoration:none;font-family:"Source Sans 3",sans-serif;font-weight:600;font-size:15.5px;border-right:1px solid #2a5890}
.nav a:last-child{border-right:0;flex:1;text-align:center}
.nav a.active{background:var(--navy-light)}
.dropdown{left:538px;top:371px;width:197px}
.dropdown a{display:block;height:37px;line-height:36px;padding-left:10px;color:#fff;text-decoration:none;font-family:"Source Sans 3",sans-serif;font-size:15.5px;letter-spacing:.3px}
.dropdown .item-green{background:var(--green);border-bottom:1px solid #fff}
.dropdown .item-navy{background:var(--navy-dark);border:1px solid #c9d5e6}

.welcome{left:120px;top:408px;font-family:"Source Sans 3",sans-serif;font-weight:600;font-size:26px;color:var(--navy);white-space:nowrap}
.intro{left:122px;top:452px;width:630px;font-size:14.5px;line-height:22px}

.card{left:133px;width:614px;height:312px;background:var(--panel);border:1px solid var(--panel-line);border-radius:8px 8px 0 0}
.card-head{height:45px;line-height:45px;padding-left:21px;border-radius:7px 7px 0 0;background:linear-gradient(var(--navy-light),var(--navy-dark));color:#fff;font-weight:700;font-size:16px;letter-spacing:.3px}
.card-photo{left:35px;top:58px;width:160px;height:108px;background:linear-gradient(#b4c2cf 0%,#c9d3db 25%,#6f8a45 30%,#5d7f38 100%);box-shadow:3px 3px 4px rgba(0,0,0,.45)}
.btn{left:72px;width:103px;height:34px;border-radius:4px;background:linear-gradient(#0d7a40,var(--green-dark));color:#fff;font-size:13.5px;letter-spacing:.5px;display:flex;align-items:center;gap:9px;padding-left:12px}
.btn svg{width:18px;height:18px}
.card-info{left:222px;top:68px;width:370px;font-size:13.5px;letter-spacing:.4px;line-height:18px}
.card-date{font-family:"Source Sans 3",sans-serif;font-weight:700;font-size:17px;letter-spacing:1px;margin-bottom:9px}
.card-info .sell{padding-left:2px}
.sale-bill{color:var(--alert);font-weight:700;font-size:14.5px;letter-spacing:0;margin:11px 0 14px 108px}
.card-info b{font-weight:700}
.pin{display:inline-block;width:10px;height:13px;vertical-align:-2px;margin-right:5px}
.when{padding-left:66px}

.widget{left:791px;width:296px;background:var(--panel);border:1px solid var(--panel-line)}
.widget-head{height:45px;line-height:45px;padding-left:17px;background:var(--green-dark);color:#fff;font-family:"Source Sans 3",sans-serif;font-weight:600;font-size:24px}
.featured-title{margin:19px 16px 0;text-align:center;font-weight:700;font-size:14.5px;line-height:18px}
.featured-photo{margin:22px auto 0;width:179px;height:109px;border:3px solid var(--navy);background:linear-gradient(#d7e3ea,#b8c7a8 45%,#6f8f4a)}
.featured-meta{margin-top:17px;text-align:center;font-size:12.5px;line-height:16px}

.seller{left:822px;top:730px;width:257px;height:72px;border-radius:4px;background:linear-gradient(#7d4a2b,#4a2413);display:flex;align-items:center;padding-left:12px;color:#fff}
.seller svg{width:58px;height:58px}
.seller-word{font-family:"Source Sans 3",sans-serif;font-weight:600;font-size:40px;line-height:38px;margin-left:12px}
.seller-link{font-size:14px;text-decoration:underline;margin-left:13px}

.testimonial-name{margin:14px 0 0 17px;font-weight:700;font-size:14px;color:#3a1a12}
.testimonial-text{margin:16px 20px 0 18px;font-size:13px;line-height:18px}

.footer{left:105px;top:1293px;color:#fff;font-size:14px;letter-spacing:.3px;line-height:20px}
.footer .legal{margin-top:4px;font-size:13.5px;line-height:18px}
.footer-brand{left:797px;top:1302px;display:flex;align-items:center;gap:10px;color:var(--footer-mark);font-family:"Source Sans 3",sans-serif;font-weight:700;font-size:21px;line-height:23px}
.footer-brand .dot{width:38px;height:38px;border-radius:50%;background:var(--footer-mark)}
.footer-brand .site{text-align:center}
</style>
</head>
<body>
<div class="stage">
  <div class="abs page"></div>

  <header>
    <div class="abs header"></div>
    <div class="abs hero" role="img" aria-label="Slideshow photo of farm fields beside a calm river"></div>
    <div class="abs hero-fade"></div>
    <div class="abs brand"><span class="brand-dot"></span><span class="brand-name">Allied Acres<br>Real Estate</span></div>
    <div class="abs brand-rule"></div>
    <div class="abs site-name">Pine Harbor<br>Auction &amp;<br>Real Estate</div>
  </header>

  <nav class="abs nav">
    <a href="#">HOME</a>
    <a href="#">UPCOMING AUCTIONS</a>
    <a href="#" style="padding:0 24px">PAST AUCTIONS</a>
    <a href="#" class="active" style="padding:0 23px">ABOUT US</a>
    <a href="#" style="padding:0 24px">SERVICES</a>
    <a href="#" style="padding:0 24px">SELLERS</a>
    <a href="#" style="padding:0 24px">BUYERS</a>
    <a href="#">CONTACT US</a>
  </nav>

  <h1 class="abs welcome">Welcome to Allied Acres Real Estate</h1>
  <div class="abs dropdown">
    <a href="#" class="item-green">Upcoming auctions</a>
    <a href="#" class="item-navy">Past auctions</a>
  </div>

  <p class="abs intro">Allied Acres - Pine Harbor Auction Company is the Southeast's premier auction company. Licensed in Georgia and South Carolina, our team has experience selling all types of assets. Whether it is an equestrian property, farm, timberland, or custom home, industrial and farm equipment, a gun or coin collection, classic cars or an estate, Pine Harbor Auction can provide you the marketing resources needed to reach qualified buyers of your particular assets.</p>

  <section class="abs card" style="top:588px">
    <div class="card-head">ART, FURNITURE AND ACCESSORIES ONLINE AUCTION</div>
    <div class="abs card-photo" role="img" aria-label="Open prairie land under a pale sky"></div>
    <div class="abs btn" style="top:187px"><svg viewBox="0 0 18 18"><rect x="2" y="3" width="10" height="12" fill="none" stroke="#fff" stroke-width="1.5"/><path d="M4 7h6M4 10h6M4 13h4" stroke="#fff"/><circle cx="14" cy="7" r="3" fill="#fff"/></svg>Details</div>
    <div class="abs btn" style="top:232px"><svg viewBox="0 0 18 18"><rect x="1.5" y="3" width="15" height="12" fill="none" stroke="#fff" stroke-width="1.5"/><path d="M3 13l4-5 3 3 2-2 3 4z" fill="#f3c24a"/></svg>Photos</div>
    <div class="abs card-info">
      <div class="card-date">THURSDAY, AUGUST 21ST AT 10:00 A.M.</div>
      <div class="sell">Selling 3120 Acres of land in tracts of 2590 Acres<br>&amp; 560 Acres</div>
      <div class="sale-bill">Click here to view Sale Bill!</div>
      <b>LIVE OFF-SITE AUCTION</b><br>
      <b>Auction Location:</b><br>
      <svg class="pin" viewBox="0 0 10 13"><path d="M5 13C2 8 0 6.5 0 4.5a5 5 0 0110 0C10 6.5 8 8 5 13z" fill="#e2173a"/><circle cx="5" cy="4.5" r="1.6" fill="#fff"/></svg>118 N Prairie Rd, Alden Flats, OK 73990<br>
      <b>Property Location:</b><br>
      <svg class="pin" viewBox="0 0 10 13"><path d="M5 13C2 8 0 6.5 0 4.5a5 5 0 0110 0C10 6.5 8 8 5 13z" fill="#e2173a"/><circle cx="5" cy="4.5" r="1.6" fill="#fff"/></svg>118 N Prairie Rd, Alden Flats, OK 73990<br>
      <div class="when">08/21/14 at 10:00 AM CDT</div>
    </div>
  </section>

  <section class="abs card" style="top:933px">
    <div class="card-head">ART, FURNITURE AND ACCESSORIES ONLINE AUCTION</div>
    <div class="abs card-photo" role="img" aria-label="Open prairie land under a pale sky"></div>
    <div class="abs btn" style="top:187px"><svg viewBox="0 0 18 18"><rect x="2" y="3" width="10" height="12" fill="none" stroke="#fff" stroke-width="1.5"/><path d="M4 7h6M4 10h6M4 13h4" stroke="#fff"/><circle cx="14" cy="7" r="3" fill="#fff"/></svg>Details</div>
    <div class="abs btn" style="top:232px"><svg viewBox="0 0 18 18"><rect x="1.5" y="3" width="15" height="12" fill="none" stroke="#fff" stroke-width="1.5"/><path d="M3 13l4-5 3 3 2-2 3 4z" fill="#f3c24a"/></svg>Photos</div>
    <div class="abs card-info">
      <div class="card-date">THURSDAY, AUGUST 21ST AT 10:00 A.M.</div>
      <div class="sell">Selling 3120 Acres of land in tracts of 2590 Acres<br>&amp; 560 Acres</div>
      <div class="sale-bill">Click here to view Sale Bill!</div>
      <b>LIVE OFF-SITE AUCTION</b><br>
      <b>Auction Location:</b><br>
      <svg class="pin" viewBox="0 0 10 13"><path d="M5 13C2 8 0 6.5 0 4.5a5 5 0 0110 0C10 6.5 8 8 5 13z" fill="#e2173a"/><circle cx="5" cy="4.5" r="1.6" fill="#fff"/></svg>118 N Prairie Rd, Alden Flats, OK 73990<br>
      <b>Property Location:</b><br>
      <svg class="pin" viewBox="0 0 10 13"><path d="M5 13C2 8 0 6.5 0 4.5a5 5 0 0110 0C10 6.5 8 8 5 13z" fill="#e2173a"/><circle cx="5" cy="4.5" r="1.6" fill="#fff"/></svg>118 N Prairie Rd, Alden Flats, OK 73990<br>
      <div class="when">08/21/14 at 10:00 AM CDT</div>
    </div>
  </section>

  <aside>
    <div class="abs widget" style="top:387px;height:321px">
      <div class="widget-head">Featured Property</div>
      <div class="featured-title">13.35 ACRES OF PRIME DEVELOP<br>&amp; 33RD STREET</div>
      <div class="featured-photo" role="img" aria-label="White farmhouse with a crowd gathered on the lawn"></div>
      <div class="featured-meta">LOTS 13 &amp; 14 FOR SALE,<br>MILLBROOK IOWA<br>Third Street, Millbrook, IA 52690</div>
    </div>

    <div class="abs seller">
      <svg viewBox="0 0 58 58"><path d="M16 20L29 8l13 12v12H16z" fill="none" stroke="#fff" stroke-width="3"/><rect x="25" y="22" width="8" height="10" fill="#fff"/><path d="M4 38l12-6 10 6 6-3 10 3 12-6v6l-12 8-10-3-6 3-10-3-12 4z" fill="#fff"/></svg>
      <div><div class="seller-word">Seller</div><div class="seller-link">Click Here For Detail</div></div>
    </div>

    <div class="abs widget" style="top:837px;left:793px;height:243px">
      <div class="widget-head" style="padding-left:25px">Testimonials Blog</div>
      <div class="testimonial-name">Dalton Reeve</div>
      <p class="testimonial-text">It is a long established fact that a reader will be distracted by the readable content of a page when looking at its layout. The point of using Lorem Ipsum is that it has a more-or-less normal distribution of letters, as opposed to using.</p>
    </div>
  </aside>

  <footer>
    <div class="abs footer">
      Pine Harbor Auction &amp; Real Estate<br>
      415 Marsh Lane, Belhaven, SC 29911<br>
      Call Today: 555.014.2200. Fax:(555)014-2203
      <div class="legal">Copyright © 2014 • Pine Harbor Auction &amp; Real Estate. • All Rights Reserved<br>Powered by: BidWorks.com &amp; VELTRIQ</div>
    </div>
    <div class="abs footer-brand"><span class="dot"></span><span>Allied Acres<br>Real Estate</span><span class="site">Pine Harbor<br>Auction &amp;<br>Real Estate</span></div>
  </footer>
</div>
</body>
</html>
```